Personal Training Studio business cards

Black logo on front. Also need: Carlyse Brondway Master Trainer, Phone: 0498315627 on the front.
On the back want the white logo and also want 10 stars or similar that can be stamped when attended Studio. The 10th start to have "Free" written under it.
Also want a line to write an appointment date and time on it.

```html
<!DOCTYPE html>
<html lang="en">
<head>
<meta charset="utf-8">
<title>Vireo Studio – Business Cards</title>
<link href="https://fonts.googleapis.com/css2?family=Open+Sans:wght@400;600;700&display=swap" rel="stylesheet">
<style>
  :root {
    --bg: #5a5a5a;
    --card-light: #f4f4f4;
    --card-dark: #050505;
    --purple: #6a3fa0;
    --green: #7cb83a;
    --ink: #333333;
    --white: #ffffff;
  }
  html, body {
    margin: 0;
    padding: 0;
    width: 1200px;
    height: 904px;
    overflow: hidden;
    background: var(--bg);
    font-family: "Open Sans", Arial, sans-serif;
  }
  .canvas {
    position: relative;
    width: 1200px;
    height: 904px;
  }
  .card {
    position: absolute;
    width: 640px;
    height: 366px;
    border-radius: 4px;
    box-shadow: 0 8px 24px rgba(0,0,0,0.35);
    overflow: hidden;
  }
  .card--back { left: 90px; top: 50px; background: var(--card-light); }
  .card--front { left: 470px; top: 488px; background: var(--card-dark); }

  .brand {
    position: absolute;
    display: flex;
    align-items: center;
    gap: 10px;
    font-weight: 700;
    color: var(--purple);
    letter-spacing: 1px;
    text-transform: uppercase;
    white-space: nowrap;
  }
  .brand__dot {
    width: 14px;
    height: 14px;
    border-radius: 50%;
    background: var(--purple);
  }
  .card--back .brand { left: 200px; top: 58px; font-size: 34px; }
  .card--front .brand { left: 0; right: 0; justify-content: center; top: 92px; font-size: 40px; }

  .stars { position: absolute; inset: 0; }
  .free {
    position: absolute;
    left: 553px;
    top: 150px;
    width: 50px;
    text-align: center;
    font-size: 12px;
    font-weight: 700;
    color: var(--green);
    letter-spacing: 0.5px;
  }

  .appointment {
    position: absolute;
    left: 36px;
    right: 30px;
    bottom: 44px;
    display: flex;
    align-items: flex-end;
    gap: 6px;
    font-size: 13px;
    color: var(--ink);
  }
  .appointment__rule {
    border-bottom: 1.5px solid var(--ink);
    height: 0;
    margin-bottom: 4px;
  }
  .appointment__rule--date { flex: 1.6; }
  .appointment__rule--time { flex: 1; }

  .divider {
    position: absolute;
    left: 150px;
    right: 150px;
    top: 190px;
    height: 2px;
    background: linear-gradient(90deg, rgba(255,255,255,0), rgba(255,255,255,0.85), rgba(255,255,255,0));
  }
  .contact {
    position: absolute;
    left: 0;
    right: 0;
    top: 222px;
    text-align: center;
  }
  .contact__name { font-size: 21px; font-weight: 700; color: var(--purple); letter-spacing: 0.5px; }
  .contact__role { font-size: 17px; color: var(--green); margin-top: 2px; }
  .contact__phone { font-size: 17px; color: var(--white); margin-top: 2px; letter-spacing: 0.5px; }
</style>
</head>
<body>
<div class="canvas">
  <section class="card card--back" aria-label="Loyalty card back">
    <div class="brand"><span class="brand__dot"></span>Vireo Studio</div>
    <svg class="stars" width="640" height="366" viewBox="0 0 640 366" aria-label="Ten stamp stars">
      <defs>
        <polygon id="star" points="0,-14 4.1,-4.3 13.3,-4.3 5.9,1.7 8.6,11.3 0,5.6 -8.6,11.3 -5.9,1.7 -13.3,-4.3 -4.1,-4.3" fill="#6a3fa0"/>
      </defs>
      <use href="#star" x="52" y="150"/>
      <use href="#star" x="100" y="198"/>
      <use href="#star" x="58" y="248"/>
      <use href="#star" x="230" y="180"/>
      <use href="#star" x="330" y="150"/>
      <use href="#star" x="410" y="150"/>
      <use href="#star" x="490" y="104"/>
      <use href="#star" x="510" y="30"/>
      <use href="#star" x="585" y="70"/>
      <use href="#star" x="578" y="130"/>
    </svg>
    <div class="free">FREE</div>
    <div class="appointment">
      <span>DATE:</span><span class="appointment__rule appointment__rule--date"></span>
      <span>TIME:</span><span class="appointment__rule appointment__rule--time"></span>
      <span>(AM/PM)</span>
    </div>
  </section>

  <section class="card card--front" aria-label="Business card front">
    <div class="brand"><span class="brand__dot"></span>Vireo Studio</div>
    <div class="divider"></div>
    <div class="contact">
      <div class="contact__name">Carlyse Brondway</div>
      <div class="contact__role">Master Trainer</div>
      <div class="contact__phone">0498315627</div>
    </div>
  </section>
</div>
</body>
</html>
```